Redesign of Pledgebloom.com

We need a redesign of some key-pages on our crowdfunding website for mobile apps, PledgeBloom.com.

- Redesign of homepage
http://www.pledgebloom.com/en

- Redesign of project submission page
http://www.pledgebloom.com/en/submit-your-app/submit-your-app

- Redesign of browsing section
http://www.pledgebloom.com/en/fund-apps

- Redesign of project funding page
http://www.pledgebloom.com/en/fund-apps/sponsor/sketch-riddler?amount=5.00

Design should be highly focused on a great user experience for users of the platform, being in principal mobile developers. So we need a great user experience for mobile developers using our service.

Benchmark designs we particularly like are:
http://www.brimwagon.com/
http://www.tradeyourtool.com/landing/
http://www.vovari.com/

Design should have a more 'fun, happy to get involved' factor as it has nox.
Updates

Target Market(s)

mobile app developers

Industry/Entity Type

Crowdfunding

Requirements
Must have
• Submission forms must have explanation fields next to the form

Homepage should have design in whihc a introductary video can be integrated

```html
<!DOCTYPE html>
<html lang="en">
<head>
<meta charset="utf-8">
<title>PledgeBloom – Crowdfunding Mobile Apps</title>
<link href="https://fonts.googleapis.com/css2?family=Comfortaa:wght@400&family=Philosopher:ital@1&family=Ubuntu:wght@400;500&display=swap" rel="stylesheet">
<style>
:root{
  --navy:#0c2a55;
  --navy-dark:#081f42;
  --brand:#0d4c8c;
  --sky:#2aa8e8;
  --sky-light:#45c0f3;
  --sky-deep:#1690d6;
  --ink:#1d2e4a;
  --white:#ffffff;
  --link-blue:#4ab6f0;
  --video-bg:#4a3a36;
}
*{margin:0;padding:0;box-sizing:border-box}
html,body{width:1200px;height:763px;overflow:hidden;background:var(--white);font-family:"Ubuntu",sans-serif}
.page{position:relative;width:1200px;height:763px}
.top-rule{position:absolute;left:0;top:0;width:100%;height:3px;background:var(--navy)}
.brand{position:absolute;left:34px;top:62px;display:flex;align-items:center;gap:12px}
.brand-mark{width:34px;height:34px;border-radius:50%;background:var(--brand)}
.brand-name{font-family:"Ubuntu",sans-serif;font-weight:500;font-size:34px;color:var(--brand)}
.util-links{position:absolute;left:588px;top:16px;font-size:15px;color:var(--ink)}
.util-links span{margin:0 8px}
.language{position:absolute;left:799px;top:11px;width:127px;height:30px;border:1px solid #c8ccd4;border-radius:6px;font-size:15px;color:var(--ink);padding:6px 0 0 11px;background:linear-gradient(#fff,#eef0f3)}
.language svg{position:absolute;right:7px;top:6px}
.account-tab{position:absolute;left:955px;top:0;width:200px;height:50px;background:var(--brand);border:2px solid var(--navy-dark);border-top:none;border-radius:0 0 16px 16px;color:var(--white);font-size:15px;padding:14px 0 0 28px}
.account-tab span{margin:0 8px}
.account-tab svg{position:absolute;right:14px;top:15px}
.main-nav{position:absolute;left:0;top:170px;width:100%;height:60px;background:linear-gradient(var(--navy),var(--navy-dark));border-bottom:2px solid #5fc6f5}
.nav-item{position:absolute;top:18px;font-size:16px;color:var(--white)}
.nav-item.active{color:var(--link-blue)}
.nav-sep{position:absolute;top:16px;width:1px;height:26px;background:#2d5a8e}
.search{position:absolute;left:916px;top:12px;width:256px;height:34px;border-radius:17px;background:var(--white);font-size:13px;color:#999;padding:10px 0 0 10px}
.search svg{position:absolute;right:10px;top:7px}
.hero{position:absolute;left:0;top:232px;width:100%;height:416px;background:linear-gradient(160deg,var(--sky-light) 0%,var(--sky) 45%,var(--sky-deep) 100%);border-bottom:2px solid #1a7fc0}
.hero-title{position:absolute;left:37px;top:28px;font-family:"Comfortaa",sans-serif;font-size:43px;color:var(--white);letter-spacing:1px}
.pitch{position:absolute;top:138px;font-family:"Philosopher",sans-serif;font-style:italic;color:var(--white)}
.pitch h2{font-weight:400;font-size:31px;color:var(--ink);margin-bottom:10px}
.pitch li{list-style:none;font-size:20px;line-height:35px}
.video{position:absolute;left:723px;top:18px;width:464px;height:379px;background:#111;border:2px solid #222}
.video-bar{height:26px;display:flex;justify-content:flex-end;gap:14px;padding:8px 8px 0;font-size:9px;color:#ddd}
.video-frame{position:absolute;left:2px;top:26px;width:456px;height:282px;background:linear-gradient(180deg,#8a4b3a 0%,var(--video-bg) 40%,#1d1f2a 100%)}
.play{position:absolute;left:50%;top:50%;transform:translate(-50%,-50%);width:70px;height:48px;border-radius:10px;background:rgba(20,20,20,.85)}
.progress{position:absolute;left:8px;right:6px;top:348px;height:4px;background:#c0141b}
.progress::before{content:"";position:absolute;left:-3px;top:-4px;width:12px;height:12px;border-radius:50%;background:#ddd}
.controls{position:absolute;left:0;right:0;bottom:0;height:22px;background:#1b1b1b;font-size:10px;color:#ccc;display:flex;align-items:center;gap:14px;padding-left:20px}
</style>
</head>
<body>
<div class="page">
  <div class="top-rule"></div>

  <header>
    <div class="brand"><span class="brand-mark"></span><span class="brand-name">PledgeBloom</span></div>
    <div class="util-links">Blog<span>|</span>Get AAA Certified</div>
    <div class="language">Language
      <svg width="18" height="18" viewBox="0 0 18 18"><circle cx="9" cy="9" r="9" fill="#111"/><path d="M5 7l4 4 4-4" stroke="#fff" stroke-width="2" fill="none"/></svg>
    </div>
    <div class="account-tab">Login<span>|</span>Register
      <svg width="20" height="20" viewBox="0 0 20 20"><circle cx="10" cy="10" r="9" fill="#5aa9e0" stroke="#fff" stroke-width="1.5"/><path d="M10 5v10M5 10h10" stroke="#fff" stroke-width="2.2"/></svg>
    </div>
  </header>

  <nav class="main-nav">
    <span class="nav-item active" style="left:25px">Home</span>
    <span class="nav-sep" style="left:91px"></span>
    <span class="nav-item" style="left:120px">About Us</span>
    <span class="nav-sep" style="left:214px"></span>
    <span class="nav-item" style="left:240px">Fund Apps</span>
    <span class="nav-sep" style="left:346px"></span>
    <span class="nav-item" style="left:370px">Submit Your App</span>
    <span class="nav-sep" style="left:524px"></span>
    <span class="nav-item" style="left:547px">Find A Developer</span>
    <span class="nav-sep" style="left:707px"></span>
    <span class="nav-item" style="left:729px">How It Works</span>
    <div class="search">Search
      <svg width="22" height="22" viewBox="0 0 22 22"><circle cx="13" cy="9" r="6" stroke="#111" stroke-width="2.4" fill="none"/><path d="M9 13l-6 6" stroke="#111" stroke-width="3"/></svg>
    </div>
  </nav>

  <section class="hero">
    <h1 class="hero-title">crowdfunding mobile apps</h1>
    <div class="pitch" style="left:37px">
      <h2>App Builders</h2>
      <ul><li>Fund your development</li><li>Get downloads</li><li>Keep 100% ownership</li></ul>
    </div>
    <div class="pitch" style="left:362px">
      <h2>Funders</h2>
      <ul><li>Get great returns on your funding</li><li>Fund per milestone</li><li>Be part of a succes story</li></ul>
    </div>

    <div class="video">
      <div class="video-bar"><span>Share</span><span>More info</span></div>
      <div class="video-frame" role="img" aria-label="Introductory video still of the founder speaking in front of a brick wall">
        <div class="play"><svg width="70" height="48" viewBox="0 0 70 48"><path d="M28 14l16 10-16 10z" fill="#fff"/></svg></div>
      </div>
      <div class="progress"></div>
      <div class="controls">
        <svg width="10" height="12" viewBox="0 0 10 12"><path d="M0 0l10 6-10 6z" fill="#ccc"/></svg>
        <svg width="14" height="12" viewBox="0 0 14 12"><path d="M0 4h3l4-4v12l-4-4H0z" fill="#ccc"/><path d="M9 3q3 3 0 6" stroke="#ccc" fill="none"/></svg>
        <span>0:00</span>
      </div>
    </div>
  </section>
</div>
</body>
</html>
```